Nirel Solutions Business Card
Stationary as well/logo for resumes, etc.
We are getting there. I need two samples...I like the black face Quorvix has going. I want the website across the bottom. I potentially want to see a black fade into a white bottom (background).
I also don't want it too busy so one color (blue) font. quorvix is close to what I am seeking
Gang,
I uploaded the files of my logo and am sorry for doing this late. What I am looking for is a business card and staionary that incorporates this. Peltcraft you are close to what I am lookign for witht he staionary- the card layout, I like tobrenik's better. In my logo there is a two tone as well, some with a black background and some with white- i want to try and explore this...

```html
<!DOCTYPE html>
<html lang="en">
<head>
<meta charset="utf-8">
<title>Nirel Solutions Business Card</title>
<link href="https://fonts.googleapis.com/css2?family=Cormorant+Garamond:ital,wght@0,500;1,500;1,600&family=EB+Garamond:ital@1&display=swap" rel="stylesheet">
<style>
  :root {
    --card-black: #000000;
    --accent-cyan: #5fd3ea;
    --band-cyan: #8fdcf0;
    --web-blue: #1b9fd2;
    --contact-white: #e8e8e8;
    --mark-grey: #3b4045;
    --foot-light: #f4f6f7;
    --foot-grey: #d9dde0;
  }
  html, body {
    margin: 0;
    padding: 0;
    width: 1200px;
    height: 686px;
    overflow: hidden;
    background: var(--card-black);
  }
  .card {
    position: relative;
    width: 1200px;
    height: 686px;
    background: var(--card-black);
    overflow: hidden;
    font-family: "Cormorant Garamond", Georgia, serif;
  }
  .brand {
    position: absolute;
    left: 66px;
    top: 50px;
    width: 280px;
    text-align: center;
  }
  .brand-dot {
    display: block;
    width: 200px;
    height: 200px;
    margin: 0 auto;
  }
  .brand-name {
    margin-top: 28px;
    color: var(--accent-cyan);
    font-size: 40px;
    font-weight: 500;
    font-style: italic;
    white-space: nowrap;
  }
  .holder-name {
    position: absolute;
    left: 340px;
    top: 14px;
    margin: 0;
    color: var(--accent-cyan);
    font-size: 70px;
    font-weight: 500;
    font-style: italic;
    letter-spacing: 1px;
    white-space: nowrap;
  }
  .holder-title {
    position: absolute;
    left: 350px;
    top: 98px;
    margin: 0;
    color: var(--accent-cyan);
    font-size: 62px;
    font-weight: 500;
    white-space: nowrap;
  }
  .contact {
    position: absolute;
    left: 643px;
    top: 192px;
    margin: 0;
    color: var(--contact-white);
    font-family: "EB Garamond", Georgia, serif;
    font-style: italic;
    font-size: 36px;
    line-height: 54px;
  }
  .contact-address { margin-bottom: 12px; }
  .contact-lines { line-height: 52px; }
  .card-band {
    position: absolute;
    left: 0;
    top: 590px;
    width: 1200px;
    height: 16px;
    background: var(--band-cyan);
  }
  .card-foot {
    position: absolute;
    left: 0;
    top: 612px;
    width: 1200px;
    height: 74px;
    background: linear-gradient(to bottom, var(--foot-light), var(--foot-grey));
  }
  .website {
    position: absolute;
    left: 0;
    top: 600px;
    width: 1200px;
    text-align: left;
    padding-left: 215px;
    box-sizing: border-box;
    color: var(--web-blue);
    font-size: 74px;
    font-weight: 600;
    font-style: italic;
    letter-spacing: 2px;
    white-space: nowrap;
  }
</style>
</head>
<body>
  <main class="card">
    <div class="brand">
      <svg class="brand-dot" viewBox="0 0 200 200" aria-hidden="true">
        <circle cx="100" cy="100" r="96" fill="var(--mark-grey)"/>
      </svg>
      <div class="brand-name">Nirel Solutions</div>
    </div>

    <h1 class="holder-name">Dorian K. Malvestro</h1>
    <h2 class="holder-title">Business Devekoper Manager</h2>

    <address class="contact">
      <div class="contact-address">
        1180 Harbor Ridge Road<br>
        Suite 310<br>
        Corvale, TX 70419
      </div>
      <div class="contact-lines">
        P : 555. 204. 7381<br>
        C : 555. 318. 6627<br>
        F : 555. 472. 1950<br>
        E : dorian@nirel-it.com
      </div>
    </address>

    <div class="card-band"></div>
    <div class="card-foot"></div>
    <div class="website">www.nirel-it.com</div>
  </main>
</body>
</html>
```